Auto glass company

BRIGHTWAY
Roving Auto Glass, LLC
555-604-1937

* Windshield Replacement
* Rock Chip Repair
Danny "K"
Brightwayrovingautoglass@example.com
* Fully Insured

This is what I would like on the card. The image is what I had before. Looking for a logo possible too, couldn’t find a place to add that on. It’s a auto glass company.

Target Market(s)

Auto glass

Industry/Entity Type

Auto glass

Contact Information for Business Card

Logo, business name, phone number, windshield replacement, rock chip repair, insured, owner name Danny K, email address brightwayrovingautoglass@example.com

Colors

Designer to choose colors to be used in the design.

Requirements
Must have
• Logo, business name, phone number, windshield replacement, rock chip repair, insured, owner name Danny K, email address brightwayrovingautoglass@example.com

```html
<!DOCTYPE html>
<html lang="en">
<head>
<meta charset="utf-8">
<title>Brightway Roving Auto Glass – Business Card</title>
<link rel="stylesheet" href="https://fonts.googleapis.com/css2?family=Montserrat:wght@400;500;600;700&display=swap">
<style>
  :root {
    --backdrop: #bdbdbd;
    --card-dark: #000000;
    --card-light: #ffffff;
    --teal: #0b8c8a;
    --ink: #1a1a1a;
    --white: #ffffff;
  }
  * { box-sizing: border-box; margin: 0; padding: 0; }
  html, body { width: 1200px; height: 1190px; overflow: hidden; }
  body {
    background: var(--backdrop);
    font-family: "Montserrat", sans-serif;
    position: relative;
  }
  .card {
    position: absolute;
    left: 150px;
    width: 900px;
    height: 514px;
    box-shadow: 0 4px 10px rgba(0,0,0,0.25);
  }
  .card--front { top: 61px; background: var(--card-dark); }
  .card--back { top: 615px; background: var(--card-light); }

  .brand {
    position: absolute;
    display: flex;
    align-items: center;
    gap: 14px;
    font-weight: 500;
    line-height: 1.25;
  }
  .brand__mark {
    width: 16px;
    height: 16px;
    flex: none;
    background: var(--teal);
  }
  .card--front .brand {
    left: 0; right: 0; top: 222px;
    justify-content: center;
    color: var(--white);
    font-size: 30px;
  }
  .card--back .brand {
    left: 560px; width: 300px; top: 196px;
    color: var(--ink);
    font-size: 26px;
  }

  .owner {
    position: absolute;
    left: 87px; top: 112px;
    font-size: 32px;
    font-weight: 700;
    color: var(--teal);
  }
  .owner__nick { color: var(--ink); }

  .services {
    position: absolute;
    left: 87px; top: 155px;
    list-style: none;
  }
  .services li {
    display: flex;
    align-items: center;
    gap: 20px;
    font-size: 27px;
    font-weight: 400;
    color: var(--ink);
    line-height: 35px;
  }
  .services svg { width: 12px; height: 14px; flex: none; }

  .contact {
    position: absolute;
    left: 87px; top: 342px;
    list-style: none;
  }
  .contact li {
    display: flex;
    align-items: center;
    gap: 18px;
    font-size: 24px;
    color: var(--ink);
    line-height: 31px;
  }
  .contact svg { width: 18px; height: 18px; flex: none; }
</style>
</head>
<body>

  <section class="card card--front" aria-label="Business card front">
    <p class="brand"><span class="brand__mark" aria-hidden="true"></span>Brightway Roving Auto Glass, LLC</p>
  </section>

  <section class="card card--back" aria-label="Business card back">
    <p class="owner">Danny <span class="owner__nick">"K"</span></p>

    <ul class="services">
      <li><svg viewBox="0 0 12 14" aria-hidden="true"><path d="M3 2 L9 7 L3 12" fill="none" stroke="var(--teal)" stroke-width="2"/></svg>Windshield Replacement</li>
      <li><svg viewBox="0 0 12 14" aria-hidden="true"><path d="M3 2 L9 7 L3 12" fill="none" stroke="var(--teal)" stroke-width="2"/></svg>Rock Chip Repair</li>
      <li><svg viewBox="0 0 12 14" aria-hidden="true"><path d="M3 2 L9 7 L3 12" fill="none" stroke="var(--teal)" stroke-width="2"/></svg>Fully Insured</li>
    </ul>

    <ul class="contact">
      <li>
        <svg viewBox="0 0 24 24" aria-hidden="true"><path d="M6.5 3.5 L9.5 3 L11 7.5 L9 9 C10 11.5 12.5 14 15 15 L16.5 13 L21 14.5 L20.5 17.5 C19.5 19.5 17 20.5 14 19 C9.5 17 7 14.5 5 10 C3.5 7 4.5 4.5 6.5 3.5 Z" fill="none" stroke="var(--teal)" stroke-width="1.6" stroke-linejoin="round"/></svg>
        555-604-1937
      </li>
      <li>
        <svg viewBox="0 0 24 24" aria-hidden="true"><rect x="3" y="5.5" width="18" height="13" rx="1.5" fill="none" stroke="var(--teal)" stroke-width="1.6"/><path d="M3.5 6.5 L12 13 L20.5 6.5" fill="none" stroke="var(--teal)" stroke-width="1.6"/></svg>
        Brightwayrovingautoglass@example.com
      </li>
    </ul>

    <p class="brand"><span class="brand__mark" aria-hidden="true"></span>Brightway Roving Auto Glass, LLC</p>
  </section>

</body>
</html>
```